Brenton Wealth Management Flow Charts

I need help creating three flow charts for my businesses website. We want them to be simple but look professional. This is for a Wealth Management firm. I will attach a word document that has all of the descriptions for everything so you know what icons to use. We just want the chart to have an icon, the names of each step and the corresponding numbers. I will also include some examples of charts we liked as well. Once the winner is selected, we will need help with additional graphic design elements for our website ASAP.
- Goudy Roman

```html
<!DOCTYPE html>
<html lang="en">
<head>
<meta charset="utf-8">
<title>Retirement Planning and Legacy Planning Flow Charts</title>
<link rel="stylesheet" href="https://fonts.googleapis.com/css2?family=Oswald:wght@300;400;500;600&family=Sorts+Mill+Goudy&family=Cormorant+Garamond:wght@600&display=swap">
<style>
  :root {
    --white: #ffffff;
    --panel-grey: #b3b3b3;
    --ink: #111111;
    --step-discovery: #fca103;
    --step-learning: #66c9cf;
    --step-planning: #029a88;
    --step-execution: #8c22a9;
    --step-alignment: #0a4c6f;
    --step-review: #ef5350;
    --flow-intro: #c5d6d1;
    --flow-beneficiaries: #9ed638;
    --flow-trusts: #3dd3a0;
    --flow-taxes: #3ad3e3;
    --flow-giving: #3ba7e5;
    --flow-charity: #1f72c2;
  }
  html, body {
    margin: 0;
    padding: 0;
    width: 860px;
    height: 1200px;
    overflow: hidden;
    background: var(--white);
  }
  .charts {
    display: block;
    width: 860px;
    height: 1200px;
  }
  .step-label {
    font-family: "Oswald", sans-serif;
    font-weight: 400;
    font-size: 35px;
    fill: var(--white);
  }
  .step-number {
    font-family: "Cormorant Garamond", serif;
    font-weight: 600;
    font-size: 76px;
    font-variant-numeric: lining-nums;
    font-feature-settings: "lnum" 1;
    fill: var(--white);
  }
  .cycle-title {
    font-family: "Oswald", sans-serif;
    font-weight: 600;
    font-size: 58px;
    fill: var(--ink);
  }
  .flow-heading {
    font-family: "Sorts Mill Goudy", serif;
    font-size: 56px;
    fill: var(--white);
  }
  .card-title {
    font-family: "Oswald", sans-serif;
    font-weight: 500;
    font-size: 38px;
  }
  .badge-number {
    font-family: "Oswald", sans-serif;
    font-weight: 500;
    font-size: 52px;
    fill: var(--white);
    text-anchor: middle;
  }
  .card { fill: var(--white); filter: url(#card-shadow); }
  .connector { fill: none; stroke-width: 14; stroke-linejoin: round; }
  .icon-line { fill: none; stroke: var(--white); stroke-width: 5; stroke-linecap: round; stroke-linejoin: round; }
  .icon-thin { fill: none; stroke-width: 4; stroke-linecap: round; stroke-linejoin: round; }
</style>
</head>
<body>
<svg class="charts" viewBox="0 0 1625 2268" xmlns="http://www.w3.org/2000/svg">
  <defs>
    <path id="cycle-segment" d="M511,214 A415,415 0 0 1 832,62 L832,0 L934,163 L832,293 L832,232 A245,245 0 0 0 649,314 L633,213 Z"/>
    <filter id="card-shadow" x="-10%" y="-10%" width="125%" height="125%">
      <feDropShadow dx="3" dy="5" stdDeviation="4" flood-color="#000" flood-opacity="0.3"/>
    </filter>
  </defs>

  <g class="retirement-cycle">
    <use href="#cycle-segment" fill="var(--step-discovery)"/>
    <use href="#cycle-segment" fill="var(--step-learning)" transform="rotate(60 832 477)"/>
    <use href="#cycle-segment" fill="var(--step-planning)" transform="rotate(120 832 477)"/>
    <use href="#cycle-segment" fill="var(--step-execution)" transform="rotate(180 832 477)"/>
    <use href="#cycle-segment" fill="var(--step-alignment)" transform="rotate(240 832 477)"/>
    <use href="#cycle-segment" fill="var(--step-review)" transform="rotate(300 832 477)"/>

    <text class="cycle-title" x="672" y="455" textLength="323" lengthAdjust="spacingAndGlyphs">THE RETIREMENT</text>
    <text class="cycle-title" x="637" y="518" textLength="393" lengthAdjust="spacingAndGlyphs">PLANNING PROCESS</text>

    <!-- 01 Discovery Meeting -->
    <g class="icon-line">
      <circle cx="652" cy="155" r="22"/>
      <line x1="668" y1="172" x2="690" y2="190" stroke-width="9"/>
      <polyline points="641,154 650,164 683,128"/>
    </g>
    <text class="step-label" x="710" y="150" textLength="112" lengthAdjust="spacingAndGlyphs">Discovery</text>
    <text class="step-label" x="710" y="182" textLength="93" lengthAdjust="spacingAndGlyphs">Meeting</text>
    <text class="step-number" x="833" y="175" textLength="65" lengthAdjust="spacingAndGlyphs">01</text>

    <!-- 02 Learning -->
    <g class="icon-line" stroke-width="4">
      <polygon points="1010,175 1058,192 1010,209 962,192"/>
      <path d="M985,201 V226 H1040 V201"/>
      <path d="M975,196 V215"/>
      <rect x="972" y="214" width="6" height="10" fill="var(--white)"/>
    </g>
    <text class="step-label" x="1022" y="263" textLength="101" lengthAdjust="spacingAndGlyphs">Learning</text>
    <text class="step-number" x="1097" y="356" textLength="70" lengthAdjust="spacingAndGlyphs">02</text>

    <!-- 03 Planning -->
    <g class="icon-line">
      <path d="M1160,488 H1130 V538 H1180 V508"/>
      <path d="M1148,523 L1152,508 L1180,480 L1190,490 L1162,518 Z"/>
    </g>
    <text class="step-label" x="1105" y="585" textLength="102" lengthAdjust="spacingAndGlyphs">Planning</text>
    <text class="step-number" x="1086" y="686" textLength="69" lengthAdjust="spacingAndGlyphs">03</text>

    <!-- 04 Execution -->
    <g class="icon-line" stroke-width="3">
      <path d="M912,752 A30,30 0 0 1 952,733"/>
      <path d="M970,752 A30,30 0 0 1 952,792"/>
      <path d="M930,793 A30,30 0 0 1 911,772"/>
      <circle cx="940" cy="763" r="12" stroke-width="8" stroke-dasharray="4 3"/>
      <circle cx="940" cy="763" r="4" fill="var(--white)"/>
    </g>
    <text class="step-label" x="885" y="830" textLength="112" lengthAdjust="spacingAndGlyphs">Execution</text>
    <text class="step-number" x="776" y="830" textLength="71" lengthAdjust="spacingAndGlyphs">04</text>

    <!-- 05 Alignment -->
    <g class="icon-line" stroke-width="3">
      <circle cx="588" cy="693" r="33"/>
      <line x1="571" y1="678" x2="605" y2="678" stroke-width="4"/>
      <line x1="575" y1="688" x2="601" y2="688" stroke-width="4"/>
      <line x1="571" y1="698" x2="605" y2="698" stroke-width="4"/>
      <line x1="575" y1="708" x2="601" y2="708" stroke-width="4"/>
    </g>
    <text class="step-label" x="580" y="777" textLength="118" lengthAdjust="spacingAndGlyphs">Alignment</text>
    <text class="step-number" x="497" y="634" textLength="69" lengthAdjust="spacingAndGlyphs">05</text>

    <!-- 06 Review -->
    <g class="icon-line" stroke-width="2.5">
      <path d="M480,360 H560 Q565,360 565,365 V406 Q565,411 560,411 H552 V437 L528,411 H480 Q475,411 475,406 V365 Q475,360 480,360 Z"/>
      <text x="480" y="392" font-size="17" fill="none" stroke="var(--white)" stroke-width="1.5" font-family="sans-serif">☆☆☆☆☆</text>
    </g>
    <text class="step-label" x="475" y="472" textLength="82" lengthAdjust="spacingAndGlyphs">Review</text>
    <text class="step-number" x="518" y="319" textLength="72" lengthAdjust="spacingAndGlyphs">06</text>
  </g>

  <g class="estate-flow">
    <rect x="0" y="1047" width="1625" height="1221" fill="var(--panel-grey)"/>

    <path class="connector" stroke="var(--flow-intro)" d="M100,1530 V1650 Q100,1685 135,1685 H375 Q408,1685 408,1652 V1540 H418"/>
    <polygon fill="var(--flow-intro)" points="415,1505 448,1538 415,1572"/>
    <text class="flow-heading" x="138" y="1542" textLength="205" lengthAdjust="spacingAndGlyphs">Legacy &amp;</text>
    <text class="flow-heading" x="138" y="1597" textLength="130" lengthAdjust="spacingAndGlyphs">Estate</text>
    <text class="flow-heading" x="138" y="1652" textLength="200" lengthAdjust="spacingAndGlyphs">Planning</text>

    <path class="connector" stroke="var(--flow-beneficiaries)" d="M440,1522 V1422 Q440,1390 472,1390 H706 Q738,1390 738,1422 V1538 H755"/>
    <polygon fill="var(--flow-beneficiaries)" points="752,1505 786,1538 752,1572"/>

    <path class="connector" stroke="var(--flow-trusts)" d="M780,1555 V1655 Q780,1685 812,1685 H1045 Q1078,1685 1078,1652 V1538 H1095"/>
    <polygon fill="var(--flow-trusts)" points="1093,1505 1127,1538 1093,1572"/>

    <path class="connector" stroke="var(--flow-taxes)" d="M1118,1522 V1422 Q1118,1390 1150,1390 H1385 Q1417,1390 1417,1422 V1655 Q1417,1685 1385,1685 H1268 V1772"/>
    <polygon fill="var(--flow-taxes)" points="1234,1768 1302,1768 1268,1802"/>

    <path class="connector" stroke="var(--flow-giving)" d="M1285,1797 H1385 Q1417,1797 1417,1829 V2060 Q1417,2092 1385,2092 H1150 Q1118,2092 1118,2060 V1945 H1103"/>
    <polygon fill="var(--flow-giving)" points="1105,1912 1072,1945 1105,1978"/>

    <path class="connector" stroke="var(--flow-charity)" d="M1076,1925 V1829 Q1076,1797 1044,1797 H812 Q780,1797 780,1829 V1945 H762"/>
    <polygon fill="var(--flow-charity)" points="764,1912 730,1945 764,1978"/>

    <!-- Card 1 Beneficiaries -->
    <rect class="card" x="470" y="1418" width="238" height="239" rx="9"/>
    <rect x="620" y="1440" width="68" height="66" rx="4" fill="var(--flow-beneficiaries)"/>
    <text class="badge-number" x="654" y="1495">1</text>
    <g class="icon-thin" stroke="var(--flow-beneficiaries)">
      <circle cx="538" cy="1455" r="14"/>
      <path d="M566,1482 Q560,1475 545,1475 H518 Q505,1475 505,1488 V1522 H545"/>
      <path d="M545,1503 Q570,1500 585,1490 Q595,1500 604,1503 V1540 Q602,1562 575,1573 Q548,1562 545,1540 Z"/>
      <path d="M585,1555 L620,1524 L600,1560"/>
    </g>
    <text class="card-title" x="497" y="1622" textLength="184" lengthAdjust="spacingAndGlyphs" fill="var(--flow-beneficiaries)">BENEFICIARIES</text>

    <!-- Card 2 Trusts -->
    <rect class="card" x="809" y="1418" width="238" height="239" rx="9"/>
    <g class="icon-thin" stroke="var(--flow-trusts)" stroke-width="3">
      <path d="M866,1466 Q890,1478 908,1472 L935,1462 Q950,1460 975,1465 L992,1456"/>
      <path d="M848,1500 L885,1512 Q900,1530 920,1540 Q945,1550 965,1525 L1012,1496"/>
      <path d="M908,1472 Q910,1480 925,1478 L945,1472 L972,1495 Q980,1505 970,1510"/>
      <path d="M893,1522 Q888,1530 898,1532 M903,1530 Q900,1540 910,1540 M915,1537 Q914,1546 925,1544"/>
    </g>
    <rect x="830" y="1572" width="67" height="65" rx="4" fill="var(--flow-trusts)"/>
    <text class="badge-number" x="863" y="1626">2</text>
    <text class="card-title" x="920" y="1626" textLength="95" lengthAdjust="spacingAndGlyphs" fill="var(--flow-trusts)">TRUSTS</text>

    <!-- Card 3 Estate Taxes & Assessment -->
    <rect class="card" x="1149" y="1418" width="238" height="239" rx="9"/>
    <rect x="1300" y="1440" width="67" height="65" rx="4" fill="var(--flow-taxes)"/>
    <text class="badge-number" x="1333" y="1495">3</text>
    <g class="icon-thin" stroke="var(--flow-taxes)" stroke-width="5">
      <polyline points="1165,1508 1212,1466 1238,1492 1282,1448"/>
      <polyline points="1263,1444 1287,1440 1281,1464"/>
      <path d="M1182,1558 V1545 H1195 V1558 M1203,1558 V1500 H1216 V1558 M1224,1558 V1520 H1237 V1558 M1245,1558 V1530 H1258 V1558 M1266,1558 V1484 H1279 V1558 H1182"/>
    </g>
    <text class="card-title" x="1188" y="1606" textLength="170" lengthAdjust="spacingAndGlyphs" fill="var(--flow-taxes)">ESTATE TAXES</text>
    <text class="card-title" x="1181" y="1641" textLength="185" lengthAdjust="spacingAndGlyphs" fill="var(--flow-taxes)">&amp; ASSESSMENT</text>

    <!-- Card 4 Annual Giving -->
    <rect class="card" x="1149" y="1825" width="238" height="239" rx="9"/>
    <g fill="var(--flow-giving)">
      <rect x="1231" y="1884" width="85" height="17"/>
      <rect x="1238" y="1907" width="31" height="44"/>
      <rect x="1278" y="1907" width="31" height="44"/>
    </g>
    <g class="icon-thin" stroke="var(--flow-giving)" stroke-width="3">
      <path d="M1272,1876 Q1252,1858 1246,1866 Q1242,1876 1272,1876 Q1302,1858 1300,1868 Q1298,1876 1272,1876"/>
    </g>
    <rect x="1170" y="1978" width="66" height="64" rx="4" fill="var(--flow-giving)"/>
    <text class="badge-number" x="1203" y="2031">4</text>
    <text class="card-title" x="1267" y="2005" textLength="98" lengthAdjust="spacingAndGlyphs" fill="var(--flow-giving)">ANNUAL</text>
    <text class="card-title" x="1279" y="2038" textLength="86" lengthAdjust="spacingAndGlyphs" fill="var(--flow-giving)">GIVING</text>

    <!-- Card 5 Donations & Charity -->
    <rect class="card" x="809" y="1825" width="238" height="239" rx="9"/>
    <rect x="962" y="1847" width="65" height="65" rx="4" fill="var(--flow-charity)"/>
    <text class="badge-number" x="994" y="1900">5</text>
    <g class="icon-thin" stroke="var(--flow-charity)">
      <path d="M906,1893 Q880,1875 879,1862 Q880,1848 893,1848 Q902,1848 906,1858 Q910,1848 920,1848 Q933,1848 933,1862 Q932,1875 906,1893 Z"/>
      <path d="M835,1922 L850,1942 L862,1932 L885,1936 Q910,1932 938,1912 Q942,1905 934,1904 L905,1918 L880,1918 L900,1912 Q905,1905 898,1902 L870,1905 Q858,1908 850,1915 Z"/>
    </g>
    <text class="card-title" x="835" y="1998" textLength="141" lengthAdjust="spacingAndGlyphs" fill="var(--flow-charity)">DONATIONS</text>
    <text class="card-title" x="835" y="2033" textLength="133" lengthAdjust="spacingAndGlyphs" fill="var(--flow-charity)">&amp; CHARITY</text>
  </g>
</svg>
</body>
</html>
```